The Best Real Estate Post Card Ever

Create a memorable and attention grabbing postcard BACK to be used the same every month and sent to 20,000 homes. The front of the postcard will change, I will make this every month. But the back I want to be known as ME and when people see it after years they instantly think of ME. This is all about branding and getting to be known as the agent to call when they need to move. I have attached styles I have used on past marketing. This design must work with both 11x8.5 and 9x6 and allow room for the postage to flow nicely.

Target Market(s)

Luxury waterfront clients

Colors
ec1f27
0255a3
ffffff

Requirements
Must have
• Clean and modern, luxury feel to it.
Nice to have
• Attention grabbing way to be remembered.
Should not have
• cheap look

```html
<!DOCTYPE html>
<html lang="en">
<head>
<meta charset="utf-8">
<title>Marcus Hollander – Postcard Back</title>
<link rel="stylesheet" href="https://fonts.googleapis.com/css2?family=Cinzel:wght@500;700&family=Montserrat:wght@400;500;800&display=swap">
<style>
  :root {
    --red: #ec1f27;
    --red-deep: #c4161d;
    --navy: #1e2f66;
    --blue: #0255a3;
    --white: #ffffff;
    --panel: #f3f3f4;
    --ink: #1e2f66;
    --muted: #3b4570;
  }
  * { box-sizing: border-box; margin: 0; padding: 0; }
  html, body { width: 1200px; height: 800px; overflow: hidden; background: #d9d9d9; }
  .postcard {
    position: relative; width: 1200px; height: 800px; overflow: hidden;
    background: var(--white); font-family: "Montserrat", Arial, sans-serif; color: var(--ink);
  }
  .postcard__art { position: absolute; inset: 0; }

  .brand-seal {
    position: absolute; left: 390px; top: 60px; width: 170px; height: 170px;
    border-radius: 50%; background: var(--white); border: 5px solid var(--navy);
    display: flex; flex-direction: column; align-items: center; justify-content: center;
    text-align: center; font-family: "Cinzel", Georgia, serif; font-weight: 700;
    color: var(--navy); line-height: 1.15;
  }
  .brand-seal__name { font-size: 21px; }
  .brand-seal__office { font-size: 12px; margin-top: 4px; }

  .features { position: absolute; left: 34px; top: 36px; width: 400px; list-style: none; }
  .feature {
    display: flex; align-items: center; gap: 14px; height: 63px;
    border-bottom: 2px solid var(--red);
  }
  .feature:last-child { border-bottom: none; }
  .feature__icon { width: 34px; height: 34px; flex: none; }
  .feature__text { font-size: 15px; line-height: 1.2; color: var(--muted); }
  .feature__text strong { font-weight: 800; color: var(--navy); }

  .headline {
    position: absolute; left: 600px; top: 305px; font-family: "Cinzel", Georgia, serif;
    font-weight: 500; color: var(--white); line-height: 1;
  }
  .headline__line { display: block; }
  .headline__line--lg { font-size: 66px; }
  .headline__line--md { font-size: 50px; margin-top: 10px; padding-left: 18px; }
  .headline__line--sm { font-size: 60px; margin-top: 8px; padding-left: 44px; }
  .headline__accent { color: var(--red); }

  .agent {
    position: absolute; left: 36px; top: 628px; color: var(--white);
  }
  .agent__name { font-family: "Cinzel", Georgia, serif; font-weight: 700; font-size: 40px; }
  .agent__titles { font-family: "Cinzel", Georgia, serif; font-weight: 500; font-size: 24px; letter-spacing: 2px; margin-top: 2px; }
  .agent__rule { width: 300px; height: 2px; background: var(--red); margin: 10px 0 8px; }
  .contact { display: flex; align-items: center; gap: 10px; font-weight: 500; }
  .contact--phone { font-size: 26px; }
  .contact--email { font-size: 19px; margin-top: 4px; }
  .contact svg { width: 18px; height: 18px; flex: none; }
</style>
</head>
<body>
<main class="postcard">
  <svg class="postcard__art" viewBox="0 0 1200 800" width="1200" height="800">
    <defs>
      <linearGradient id="sunsetHome" x1="0" y1="0" x2="0" y2="1">
        <stop offset="0" stop-color="#6e6fa0"/>
        <stop offset="0.35" stop-color="#e9a77c"/>
        <stop offset="0.6" stop-color="#7b6b68"/>
        <stop offset="1" stop-color="#3f6a3c"/>
      </linearGradient>
      <linearGradient id="fadedHome" x1="0" y1="0" x2="1" y2="1">
        <stop offset="0" stop-color="#f6f6f7"/>
        <stop offset="1" stop-color="#e4e5e8"/>
      </linearGradient>
      <linearGradient id="agentPortrait" x1="0" y1="0" x2="0" y2="1">
        <stop offset="0" stop-color="#8a8f96"/>
        <stop offset="1" stop-color="#4a4f57"/>
      </linearGradient>
    </defs>

    <!-- navy body -->
    <rect class="field-navy" x="300" y="0" width="900" height="800" fill="var(--navy)"/>

    <!-- home exterior photo area -->
    <path role="img" aria-label="Photo of a waterfront home at sunset"
          d="M300,0 H1200 V70 C1020,200 820,270 540,320 L300,340 Z" fill="url(#sunsetHome)"/>

    <!-- white postage field with red divider -->
    <path d="M1200,112 C1050,330 850,520 540,650 V800 H1200 Z" fill="var(--red)"/>
    <path d="M1200,138 C1060,350 860,540 560,668 V800 H1200 Z" fill="var(--white)"/>

    <!-- feature panel -->
    <path role="img" aria-label="Faded photo of a home behind the feature list"
          d="M0,0 H320 C480,150 545,400 525,640 L0,640 Z" fill="url(#fadedHome)"/>

    <!-- contact band -->
    <path d="M0,606 L560,580 V800 H0 Z" fill="var(--red)"/>
    <path d="M0,620 L560,594 V800 H0 Z" fill="var(--navy)"/>

    <!-- agent portrait -->
    <path role="img" aria-label="Portrait of the agent holding his young son"
          d="M500,800 V640 C520,580 560,560 600,570 C640,530 720,530 760,580 C800,600 820,650 820,720 V800 Z"
          fill="url(#agentPortrait)"/>
  </svg>

  <div class="brand-seal">
    <span class="brand-seal__name">Marcus<br>Hollander</span>
    <span class="brand-seal__office">Harborline Realty</span>
  </div>

  <ul class="features">
    <li class="feature">
      <svg class="feature__icon" viewBox="0 0 24 24"><path fill="var(--red)" d="M12 2l3 6.5 7 .8-5.2 4.8 1.4 7L12 17.6 5.8 21l1.4-7L2 9.3l7-.8z"/></svg>
      <span class="feature__text"><strong>200+</strong> 5star online reviews</span>
    </li>
    <li class="feature">
      <svg class="feature__icon" viewBox="0 0 24 24"><path fill="var(--red)" d="M12 2a7 7 0 0 0-7 7c0 5 7 13 7 13s7-8 7-13a7 7 0 0 0-7-7zm0 9.5A2.5 2.5 0 1 1 12 6.5a2.5 2.5 0 0 1 0 5z"/></svg>
      <span class="feature__text">Coral Bay County resident<br><strong>20+ years</strong></span>
    </li>
    <li class="feature">
      <svg class="feature__icon" viewBox="0 0 24 24"><circle cx="12" cy="12" r="9" fill="none" stroke="var(--red)" stroke-width="2.5"/><circle cx="12" cy="12" r="4" fill="var(--red)"/></svg>
      <span class="feature__text"><strong>Certified</strong> Luxury home<br>marketing specialist</span>
    </li>
    <li class="feature">
      <svg class="feature__icon" viewBox="0 0 24 24"><rect x="3" y="5" width="18" height="16" rx="2" fill="none" stroke="var(--red)" stroke-width="2"/><path d="M3 10h18M8 3v4M16 3v4" stroke="var(--red)" stroke-width="2"/></svg>
      <span class="feature__text"><strong>Available 7days a week</strong><br>from 8am till midnight</span>
    </li>
    <li class="feature">
      <svg class="feature__icon" viewBox="0 0 24 24"><circle cx="12" cy="12" r="9" fill="none" stroke="var(--red)" stroke-width="2"/><path d="M15 8.5c-.6-1-1.7-1.5-3-1.5-1.7 0-3 .9-3 2.3 0 3 6 1.7 6 4.7 0 1.4-1.3 2.3-3 2.3-1.4 0-2.6-.6-3.1-1.6M12 5.5v13" fill="none" stroke="var(--red)" stroke-width="1.8"/></svg>
      <span class="feature__text"><strong>$20,000,000+</strong> in pending/sold<br>sales so far in 2021</span>
    </li>
    <li class="feature">
      <svg class="feature__icon" viewBox="0 0 24 24"><rect x="2" y="7" width="20" height="14" rx="2" fill="none" stroke="var(--red)" stroke-width="2"/><path d="M8 7l1.5-3h5L16 7" fill="none" stroke="var(--red)" stroke-width="2"/><circle cx="12" cy="14" r="3.5" fill="none" stroke="var(--red)" stroke-width="2"/></svg>
      <span class="feature__text"><strong>Professional photography</strong><br>included with every listing</span>
    </li>
    <li class="feature">
      <svg class="feature__icon" viewBox="0 0 24 24"><rect x="4" y="2" width="16" height="20" rx="2" fill="none" stroke="var(--red)" stroke-width="2"/><path d="M8 8h8M8 12h8M8 16h5" stroke="var(--red)" stroke-width="2"/></svg>
      <span class="feature__text"><strong>Hassle free</strong> listing agreements,<br>cancel anytime with no fees</span>
    </li>
    <li class="feature">
      <svg class="feature__icon" viewBox="0 0 24 24"><path fill="var(--red)" d="M2 10h4v11H2zM8 21V10l5-8c1.5 0 2.5 1 2 3l-1 4h6c1.2 0 2 1 1.8 2.2l-1.6 8A2 2 0 0 1 18.2 21z"/></svg>
      <span class="feature__text"><strong>5star guarantee</strong> - if i don't meet<br>your expectations, you don't pay me</span>
    </li>
  </ul>

  <h1 class="headline">
    <span class="headline__line headline__line--lg">Results</span>
    <span class="headline__line headline__line--md">That <span class="headline__accent">Move</span></span>
    <span class="headline__line headline__line--sm">You</span>
  </h1>

  <section class="agent">
    <h2 class="agent__name">Marcus Hollander,</h2>
    <p class="agent__titles">CRS, ABR, SRS, PSA</p>
    <div class="agent__rule"></div>
    <p class="contact contact--phone">
      <svg viewBox="0 0 24 24"><path fill="var(--red)" d="M6.6 10.8a15 15 0 0 0 6.6 6.6l2.2-2.2c.3-.3.7-.4 1-.2 1.1.4 2.3.6 3.6.6.6 0 1 .4 1 1V20c0 .6-.4 1-1 1A17 17 0 0 1 3 4c0-.6.4-1 1-1h3.5c.6 0 1 .4 1 1 0 1.3.2 2.5.6 3.6.1.3 0 .7-.2 1z"/></svg>
      (555) 014-2290
    </p>
    <p class="contact contact--email">
      <svg viewBox="0 0 24 24"><rect x="2" y="5" width="20" height="14" rx="1.5" fill="var(--red)"/><path d="M2.5 6l9.5 7 9.5-7" fill="none" stroke="var(--navy)" stroke-width="1.6"/></svg>
      Marcus@HarborlineRealty.net
    </p>
  </section>
</main>
</body>
</html>
```